Business Cards for accounting firm

Need a file and design that we can update for our employees when we get a design we like. Logo is attached.
Megan Tolliver CPA
Owner
P.O. Box 918
Perrysburg OH 43617
4195550148
megan@brindlecrestltd.com
www.brindlecrestltd.com
Industry/Entity Type
Accounting

```html
<!DOCTYPE html>
<html lang="en">
<head>
<meta charset="utf-8">
<title>Brindlecrest Dental CPA's Ltd. – Business Card</title>
<link rel="stylesheet" href="https://fonts.googleapis.com/css2?family=Lato:ital,wght@0,300;0,400;1,300;1,400&family=Open+Sans:wght@400&display=swap">
<style>
  :root {
    --page: #ffffff;
    --cream: #f3efe6;
    --olive: #a3a542;
    --pale-yellow: #dfe27a;
    --dark-green: #82a64a;
    --mid-green: #9fc04a;
    --lime: #bad24c;
    --sky: #8fc8d5;
    --teal: #77bec9;
    --deep-blue: #5aa7c7;
    --logo-grey: #66635e;
    --name-blue: #5aa1c2;
    --label-grey: #9a9792;
    --value-dark: #2f2e2c;
    --white: #ffffff;
  }
  * { margin: 0; padding: 0; box-sizing: border-box; }
  html, body {
    width: 1200px;
    height: 1000px;
    overflow: hidden;
    background: var(--page);
  }
  .canvas {
    position: relative;
    width: 1200px;
    height: 1000px;
  }
  .card {
    position: absolute;
    left: 220px;
    width: 782px;
    height: 468px;
    overflow: hidden;
  }
  .card--front { top: 22px; }
  .card--back { top: 512px; background: var(--cream); }

  .card__backdrop {
    position: absolute;
    inset: 0;
    background: linear-gradient(35deg,
      var(--deep-blue) 0%,
      var(--teal) 14%,
      var(--sky) 26%,
      var(--cream) 40%,
      var(--lime) 56%,
      var(--mid-green) 70%,
      var(--dark-green) 82%,
      var(--pale-yellow) 92%,
      var(--olive) 100%);
  }

  .wordmark {
    position: absolute;
    font-family: "Open Sans", sans-serif;
    font-weight: 400;
    font-size: 38px;
    line-height: 1.12;
    letter-spacing: 0.2px;
  }
  .wordmark--front { left: 30px; top: 345px; color: var(--white); }
  .wordmark--back { left: 86px; top: 72px; color: var(--logo-grey); }

  .contact {
    position: absolute;
    left: 91px;
    top: 250px;
    font-family: "Lato", sans-serif;
    font-style: italic;
  }
  .contact__name {
    font-size: 32px;
    font-weight: 400;
    color: var(--name-blue);
    line-height: 1;
    margin-bottom: 22px;
  }
  .contact__role {
    font-size: 15px;
    font-weight: 300;
    color: var(--label-grey);
  }
  .contact__line {
    font-size: 20px;
    line-height: 35px;
    font-weight: 300;
    color: var(--value-dark);
  }
  .contact__label { color: var(--label-grey); }
</style>
</head>
<body>
<div class="canvas">

  <section class="card card--front">
    <div class="card__backdrop" role="img" aria-label="Decorative sweep of blue, cream and green bands"></div>
    <div class="wordmark wordmark--front">Brindlecrest<br>Dental CPA's Ltd.</div>
  </section>

  <section class="card card--back">
    <div class="wordmark wordmark--back">Brindlecrest<br>Dental CPA's Ltd.</div>
    <div class="contact">
      <p class="contact__name">Megan Tolliver CPA <span class="contact__role">owner</span></p>
      <p class="contact__line"><span class="contact__label">phone:</span> 4195550148</p>
      <p class="contact__line"><span class="contact__label">email:</span> megan@brindlecrestltd.com</p>
      <p class="contact__line"><span class="contact__label">web:</span> www.brindlecrestltd.com</p>
      <p class="contact__line"><span class="contact__label">mail:</span> P.O. Box 918, Perrysburg OH 43617</p>
    </div>
  </section>

</div>
</body>
</html>
```